Business Cards - New Logo Rebranding

Hello We know have a red and blue logo and are looking to create new cards. We are looking for the best creativity of the new logo merged with some of the existing artwork provided.

Target Market(s)

Realtors

Industry/Entity Type

Real Estate

Contact Information for Business Card

New logo with rebranded colors

Requirements
Must have
• Creative use of the new logo

```html
<!DOCTYPE html>
<html lang="en">
<head>
<meta charset="utf-8">
<title>Summit Crest Business Card</title>
<link rel="stylesheet" href="https://fonts.googleapis.com/css2?family=Roboto:wght@400;500;700;900&display=swap">
<style>
  :root {
    --stage: #b3b3b3;
    --red: #e0363d;
    --blue: #0a6fbd;
    --white: #ffffff;
    --ink: #111111;
    --badge: #b9b9b9;
  }
  * { margin: 0; padding: 0; box-sizing: border-box; }
  html, body { width: 1200px; height: 1200px; overflow: hidden; }
  body { background: var(--stage); font-family: "Roboto", Arial, sans-serif; position: relative; }
  .side-label { position: absolute; top: 230px; width: 200px; text-align: center; font-weight: 700; font-size: 20px; color: var(--ink); letter-spacing: .5px; }
  .card { position: absolute; width: 377px; height: 636px; background: var(--white); overflow: hidden; }
  .card > svg { position: absolute; left: 0; top: 0; }
  .t { position: absolute; left: 0; right: 0; text-align: center; }
  .brand-mark { position: absolute; border-radius: 50%; border: 5px solid var(--red); background: var(--blue); }
  .brand-name { font-weight: 900; font-size: 25px; color: var(--blue); letter-spacing: 1px; }

  .card-front { left: 182px; top: 299px; }
  .card-front .brand-mark { left: 131px; top: 56px; width: 88px; height: 88px; }
  .card-front .brand-name { top: 162px; }
  .person-name { top: 351px; color: var(--white); font-weight: 700; font-size: 22px; }
  .person-title { top: 378px; color: var(--white); font-size: 16px; }
  .contact-phone { top: 491px; color: var(--white); font-weight: 700; font-size: 15.5px; }
  .contact-line { color: var(--white); font-size: 15.5px; }
  .contact-email { top: 517px; }
  .contact-web { top: 541px; }
  .service-list { top: 608px; color: var(--red); font-weight: 500; font-size: 12.5px; letter-spacing: .3px; }

  .card-back { left: 624px; top: 311px; }
  .headline { top: 10px; color: var(--red); font-size: 16px; font-weight: 500; }
  .headline b { font-weight: 900; }
  .why-title { top: 58px; color: var(--white); font-weight: 700; font-size: 21px; }
  .benefit { color: var(--white); font-size: 13px; font-weight: 500; }
  .benefit::before { content: "\2713"; font-weight: 700; margin-right: 7px; }
  .reviews-count { top: 303px; color: var(--white); font-weight: 700; font-size: 20px; }
  .reviews-source { top: 331px; color: var(--white); font-weight: 700; font-size: 15px; }
  .card-back .brand-mark { left: 147px; top: 440px; width: 82px; height: 82px; }
  .card-back .brand-name { top: 528px; font-size: 22px; }
  .rule { position: absolute; left: 30px; width: 318px; top: 583px; height: 2px; background: var(--red); }
  .badge { position: absolute; top: 592px; width: 36px; height: 36px; border-radius: 50%; background: var(--badge); border: 2px solid var(--blue); }
  .badge.wide { width: 50px; border-radius: 6px; }
</style>
</head>
<body>
  <div class="side-label" style="left:254px">FRONT</div>
  <div class="side-label" style="left:708px">BACK</div>

  <section class="card card-front">
    <svg width="377" height="636" viewBox="0 0 377 636" aria-hidden="true">
      <path d="M0 205 C 90 292, 270 290, 377 125 L377 595 L0 595 Z" fill="var(--red)"/>
      <path d="M0 222 C 90 309, 275 305, 377 146" fill="none" stroke="var(--white)" stroke-width="4"/>
    </svg>
    <div class="brand-mark"></div>
    <div class="t brand-name">SUMMIT CREST</div>
    <div class="t person-name">DANA MORALES</div>
    <div class="t person-title">CERTIFIED MOLD INSPECTOR</div>
    <div class="t contact-phone">800.555.0142 | 562.555.0198</div>
    <div class="t contact-line contact-email">dmorales@summitcrestinspect.com</div>
    <div class="t contact-line contact-web">www.SummitCrestInspect.com</div>
    <div class="t service-list">HOME • SEWER • MOLD • COMMERCIAL • TERMITE • ROOF</div>
  </section>

  <section class="card card-back">
    <svg width="378" height="636" viewBox="0 0 378 636" aria-hidden="true">
      <rect x="0" y="41" width="378" height="595" fill="var(--blue)"/>
      <path d="M0 500 C 90 355, 300 355, 378 455 L378 636 L0 636 Z" fill="var(--white)"/>
      <path d="M0 512 C 90 370, 295 368, 378 468" fill="none" stroke="var(--blue)" stroke-width="5"/>
    </svg>
    <div class="t headline"><b>CALIFORNIA'S #1</b> INSPECTION COMPANY!</div>
    <div class="t why-title">Why Choose the Summit Crest...</div>
    <div class="t benefit" style="top:108px">Performing Inspections Since 1984</div>
    <div class="t benefit" style="top:141px">HomeCert Certified Master/ Professional Inspectors</div>
    <div class="t benefit" style="top:170px">500,000+ Inspections Completed Statewide</div>
    <div class="t benefit" style="top:198px">Request of Repairs Pricer Report</div>
    <div class="t benefit" style="top:226px">90-Day Inspection Guarantees</div>
    <div class="t benefit" style="top:255px">Federally Licensed Drone Roof Inspectors upon request</div>
    <div class="t reviews-count">5,000+ 5-Star</div>
    <div class="t reviews-source">Reviews on Rateline &amp; Starboard</div>
    <div class="brand-mark"></div>
    <div class="t brand-name">SUMMIT CREST</div>
    <div class="rule"></div>
    <div class="badge" style="left:34px"></div>
    <div class="badge" style="left:85px"></div>
    <div class="badge" style="left:138px"></div>
    <div class="badge wide" style="left:195px"></div>
    <div class="badge" style="left:270px"></div>
    <div class="badge" style="left:318px;width:28px;height:28px;top:596px"></div>
  </section>
</body>
</html>
```